Brightwell Capital websites

We need a website design for a finance company based on Gold Coast. Basically need 4 homepages....one for their main website Brightwell Capital Group and then 3 others all based on the same template for Brightwell Lending, Brightwell Invoicing and Brightwell Debt Management.

Target Market(s)

Adults based in western speaking countries who require fast loans.

Industry/Entity Type

Financial

Number of Pages Required

4 pages

Requirements
Must have
• ? Brightwell Capital Group are after 4 websites designed for the below:
o Brightwell Capital Group Pty Ltd
o Brightwell Lending Pty Ltd
o Brightwell Debt Management Pty Ltd
o Brightwell Invoicing Pty Ltd
Website 1 – Brightwell Capital Group Pty Ltd
Overview
The Brightwell Capital Group Pty Ltd website will act as the ‘fronting/summary site’ so should be kept as clean and simple as possible, very little text.
o The company name Brightwell Capital Group and logo at the top (ATTACHED Brightwellcapgrp_colored_shadow.jpg)
o Our phone number & email address at the top of the page also. (just use dummy ones for design)
o Perhaps a few lines under the phone number/email/logo etc explaining that Brightwell Capital Group is the parent company to Brightwell Lending, Brightwell Invoicing and Brightwell Debt Management.
o Then we just want three large, clear icons down the left hand side of the page. Each icon will be the logo of our businesses eg Brightwell Lending, Brightwell Debt Management and Brightwell Invoicing (all logos are attached). There will then be a few lines next to the logo saying ‘Click here to go to Brightwell Lending/Brightwell Invoicing/Brightwell Debt Management’, and a few lines about each company.
• Some icons and containers will be designed for homepage
? Brightwell Lending (image/description/click here)
? Brightwell Debt Management (image/description/click here)
? Brightwell Invoicing (image/description/click here)

Website 2 – Brightwell Lending Pty Ltd
Overview
We also require a separate site for each of the 3 businesses; ie a site for Brightwell Lending, a site for Brightwell Debt Management and a site for Brightwell Invoicing. These sites need to be very easy to navigate, clear and professional looking. We would like them to look something like the screenshot below.
Site Map
• Home
• Frequently Asked Questions
• Corporate Information
• Promotions and Latest News
• Testimonials
• Careers
• Contact Us

• The bold logo in the left hand corner. It stands out.
• The core info below the logo (ie. phone number, email address etc)
• The tabs at the top of the page ‘home, corporate etc’
• The big space for an image (or series of images)
• The space under the picture for your body copy.
• Under the logo (in the strip down the left hand side of the page…or somewhere highly visible), we would like 2 big icons with the text ‘For loans over $5000, click here’ and ‘For loans under $5000, click here’). This needs to be the focus of this page!! This is very important. Then, once customers have clicked on either icon they will be taken through to an online form they need to complete. There will be 2 different forms – 1 for loans under $5000 and 1 for loans over $5000.
• We will definitely be inserting the logos of the companies we arrange loans for next to the body copy (as KRN have done above – see how they have ZEV and other company’s logos inserted). We will not put too much copy here however as we really want the attention to be on the 2 icons mentioned above.
• We would like space for a large image (or series of images…not sure yet) under the tabs.
• Area at the bottom (down left side) of homepage a statement promoting other business eg. “Brightwell Capital Group, your one-stop-shop for financial services. Want to know what else we can do for you? Click on the below icons to find out” (then insert the logos for the other businesses).
• Some icons will be designed for homepage
? For Loans over $5000, click here
? For Loans under $5000, click here

Website 3 – Brightwell Debt Management Pty Ltd
Overview
We require a separate site for each of the 3 businesses; ie a site for Brightwell Lending, a site for Brightwell Debt Management and a site for Brightwell Invoicing. These sites need to be very easy to navigate, clear and professional looking. We would like them to look something like the screenshot in the word doc.

Site Map
• Home
• Corporate Information
• Testimonials
• Careers
• Contact Us

Design/Content Brief
• Rest of area will be used for content.

Website 4 – Brightwell Invoicing Pty Ltd
Overview

Site Map
• Home
• Corporate Information
• Testimonials
• Careers
• Contact Us

Design/Content Brief

```html
<!DOCTYPE html>
<html lang="en">
<head>
<meta charset="utf-8">
<title>Brightwell Capital Group</title>
<link href="https://fonts.googleapis.com/css2?family=Noto+Sans:wght@400;600&display=swap" rel="stylesheet">
<style>
:root{
  --page:#ffffff;
  --panel-top:#d4d4d4;
  --panel-bottom:#8c8c8c;
  --panel-edge:#5a5a5a;
  --rule:#8a8a8a;
  --label:#4a4a4a;
  --bar-top:#4a4a4a;
  --bar-bottom:#1f1f1f;
  --intro-bg:#a9a9a9;
  --ink:#111111;
  --card-bg:#e6e6e6;
  --card-ink:#2d3a8c;
  --link:#c8102e;
  --divider:#dcdcdc;
  --footer-top:#5d639f;
  --footer-bottom:#2e356f;
  --footer-ink:#7a80b4;
  --navy:#16264a;
  --pig-a:#dde3f0;
  --pig-b:#3b4d9a;
  --lend:#7a1420;
  --debt:#e0641a;
  --invoice:#1f7a32;
}
*{box-sizing:border-box;margin:0;padding:0}
html,body{width:1200px;height:944px;overflow:hidden;background:var(--page)}
body{position:relative;font-family:"Noto Sans",sans-serif}

.contact-panel{position:absolute;left:24px;top:28px;width:739px;height:298px;
  background:linear-gradient(var(--panel-top),var(--panel-bottom));
  border:2px solid var(--panel-edge);border-bottom:0;border-radius:6px 6px 0 0}
.contact-label{position:absolute;left:22px;font-size:20px;line-height:24px;color:var(--label)}
.contact-value{position:absolute;left:22px;color:#fff;white-space:nowrap}
.phone-label{top:12px}
.phone-value{top:36px;font-size:38px;line-height:46px}
.email-label{top:107px}
.email-value{top:133px;font-size:26px;line-height:32px}
.rule{position:absolute;left:16px;right:18px;height:3px;background:var(--rule)}
.rule-1{top:94px}.rule-2{top:174px}
.intro{position:absolute;left:16px;top:194px;width:702px;height:82px;
  background:var(--intro-bg);opacity:.85;padding:8px 12px;
  font-size:16px;line-height:21.6px;color:var(--ink);overflow:hidden}

.header-bar{position:absolute;left:24px;top:326px;width:1158px;height:34px;
  background:linear-gradient(var(--bar-top),var(--bar-bottom));border-radius:0 0 8px 8px}

.brand{position:absolute;left:792px;top:24px;width:390px;height:300px}
.brand-art{position:absolute;left:6px;top:0;width:220px;height:220px;border-radius:50%;
  background:radial-gradient(circle at 45% 45%,var(--pig-b),var(--pig-a) 72%,transparent 73%)}
.brand-name{position:absolute;left:10px;top:230px;font-size:28px;line-height:36px;font-weight:600;color:var(--navy);white-space:nowrap}

.divider{position:absolute;top:384px;width:4px;height:404px;background:var(--divider)}
.card{position:absolute;top:396px;width:326px}
.card-art{height:166px;width:166px;margin:0 0 0 20px;border-radius:50%;
  background:radial-gradient(circle at 45% 45%,var(--pig-b),var(--pig-a) 72%,transparent 73%)}
.card-name{height:76px;padding:14px 0 0 10px;font-size:19px;line-height:26px;font-weight:600;white-space:nowrap}
.card-body{background:var(--card-bg);height:150px;padding:12px 16px;color:var(--card-ink);font-size:16px;line-height:21.6px}
.card-body p{width:280px;height:87px;overflow:hidden}
.card-link{display:block;margin-top:14px;font-size:21px;line-height:26px;color:var(--link);text-decoration:none}
.name-lend{color:var(--lend)}.name-debt{color:var(--debt)}.name-invoice{color:var(--invoice)}

.site-footer{position:absolute;left:24px;top:853px;width:1158px;height:45px;border-radius:6px;
  background:linear-gradient(var(--footer-top),var(--footer-bottom));
  color:var(--footer-ink);font-size:13px;display:flex;align-items:center;justify-content:center}
</style>
</head>
<body>
<header>
  <section class="contact-panel">
    <span class="contact-label phone-label">Phone</span>
    <span class="contact-value phone-value">555 0193726</span>
    <div class="rule rule-1"></div>
    <span class="contact-label email-label">E - mail</span>
    <span class="contact-value email-value">info@brightwellcapitalgroup.com.au</span>
    <div class="rule rule-2"></div>
    <p class="intro">Lorem ipsum dolor sit amet, consectetur adipiscing elit. Integer feugiat, nisi in ullamcorper suscipit, justo justo luctus sapien, nec faucibus sapien nunc a diam. Morbi eu dolor quis justo vestibulum commodo. Praesent lacinia, dui sit</p>
  </section>
  <div class="brand">
    <div class="brand-art" role="img" aria-label="Brand mascot illustration"></div>
    <span class="brand-name">Brightwell Capital Group</span>
  </div>
  <div class="header-bar"></div>
</header>

<main>
  <article class="card" style="left:58px">
    <div class="card-art" role="img" aria-label="Brightwell Lending mascot illustration"></div>
    <div class="card-name name-lend">Brightwell Lending</div>
    <div class="card-body">
      <p>Lorem ipsum dolor sit amet, consectetur adipiscing elit. Integer feugiat, nisi in ullamcorper suscipit, justo justo luctus sapien,</p>
      <a class="card-link" href="#">Click here »</a>
    </div>
  </article>
  <div class="divider" style="left:406px"></div>
  <article class="card" style="left:434px">
    <div class="card-art" role="img" aria-label="Brightwell Debt Management mascot illustration"></div>
    <div class="card-name name-debt">Brightwell Debt Management</div>
    <div class="card-body">
      <p>Lorem ipsum dolor sit amet, consectetur adipiscing elit. Integer feugiat, nisi in ullamcorper suscipit, justo justo luctus sapien,</p>
      <a class="card-link" href="#">Click here »</a>
    </div>
  </article>
  <div class="divider" style="left:782px"></div>
  <article class="card" style="left:810px;width:349px">
    <div class="card-art" role="img" aria-label="Brightwell Invoicing mascot illustration"></div>
    <div class="card-name name-invoice">Brightwell Invoicing</div>
    <div class="card-body">
      <p>Lorem ipsum dolor sit amet, consectetur adipiscing elit. Integer feugiat, nisi in ullamcorper suscipit, justo justo luctus sapien,</p>
      <a class="card-link" href="#">Click here »</a>
    </div>
  </article>
</main>

<footer class="site-footer">Copyright © 2009 &nbsp;Brightwell Capital Group</footer>
</body>
</html>
```